Animal Facility Brochure for Pet Boarding, Boutique, Doggie Daycare, Grooming

This brochure is for a Doggie Daycare, Pet Grooming, Dog Boarding & Pet Boutique for the Hollandale Pet Manor & Spa.

Hi there! I am in need of a brochure done for my new up and coming business.
The business will involve Dog/Cat Grooming, Dog Boarding, Doggie Daycare, & a small pet boutique. I am looking for something that stands out and is modern and chic and follows the look of the pictures i have posted (Pippin and Rue) . My color scheme of my business is gray & white. Also i need the brochure to be easily able to understand what we are trying to get across and is easy to read. I am very proud of my logo that was created using sketch hive and would love that incorporated. also i have attached the information that will need to be in the brochure for the client. I am looking for someone who can devote some time working with me on this because this is my first time. I am sure there will need to be some changes so i need someone who is patient. The picture of the projected look of my sign is gearing more towards something clean and modern.

Pet Care

f5f5f5
f8f8f8
dbdbdb
959595
aaaaaa
85abd2
cedeed
eaf1f7

• File nine for Grooming, Boarding, Daycare, Pet Boutique

```html
<!DOCTYPE html>
<html lang="en">
<head>
<meta charset="utf-8">
<title>Hollandale Pet Manor &amp; Spa — Trifold Brochure</title>
<link rel="stylesheet" href="https://fonts.googleapis.com/css2?family=Lato:wght@400;700&family=Oswald:wght@300;400&display=swap">
<style>
  :root {
    --page-bg: #dbdbdb;
    --panel: #ffffff;
    --panel-shade: #f5f5f5;
    --blue: #85abd2;
    --blue-soft: #cedeed;
    --blue-pale: #eaf1f7;
    --ink: #1e1e1e;
    --brand: #4a3a30;
    --grey: #959595;
    --grey-light: #aaaaaa;
  }
  * { box-sizing: border-box; margin: 0; padding: 0; }
  html, body { width: 1200px; height: 2400px; overflow: hidden; }
  body {
    background: var(--page-bg);
    font-family: "Lato", sans-serif;
    color: var(--ink);
    position: relative;
  }
  .brochure {
    position: absolute; left: 40px; top: 802px;
    width: 1120px; height: 796px;
    display: flex;
    background: var(--panel);
    box-shadow: 0 10px 30px rgba(0,0,0,.18);
  }
  .panel { position: relative; width: 373.33px; height: 100%; overflow: hidden; background: var(--panel); }
  .panel--middle { background: linear-gradient(90deg, #ececec 0%, #fafafa 8%, #fff 20%); }
  .panel--cover { background: linear-gradient(90deg, #efefef 0%, #fbfbfb 8%, #fff 20%); }
  .bottom-band { position: absolute; left: 0; right: 0; bottom: 0; height: 20px; background: var(--blue); }

  /* left panel */
  .photo-grid {
    position: absolute; left: 21px; top: 31px;
    display: grid; grid-template-columns: 161px 161px; gap: 7px;
  }
  .photo { width: 161px; height: 161px; }
  .photo--dogs { background: linear-gradient(160deg, #efe7de, #b88a5c 60%, #d9c7b2); }
  .photo--cat-bowl { background: linear-gradient(160deg, #e6e2dd, #cfcac4 50%, #e2d84a 85%); }
  .photo--kittens { background: linear-gradient(160deg, #d8cfc6, #b58a62 55%, #8b6c55); }
  .photo--grey-cat { background: linear-gradient(160deg, #e9e9e9, #8f8f8f 55%, #cfcfcf); }

  .section-title {
    position: absolute; left: 0; right: 0; top: 430px;
    display: flex; align-items: center; justify-content: center; gap: 10px;
    font-family: "Oswald", sans-serif; font-weight: 300; font-size: 23px; color: var(--blue);
  }
  .flourish { display: inline-block; width: 30px; height: 8px; border-radius: 4px; background: var(--blue-soft); }
  .mission-text {
    position: absolute; left: 22px; right: 22px; top: 478px;
    font-size: 13.6px; line-height: 16.4px; text-align: justify; color: var(--ink);
  }

  /* middle panel */
  .ornament { display: block; margin: 0 auto; width: 92px; height: 14px; border-radius: 7px; background: var(--panel-shade); border: 1px solid #e4e4e4; }
  .hours { position: absolute; left: 0; right: 0; top: 78px; text-align: center; }
  .hours__label { margin-top: 22px; font-family: "Oswald", sans-serif; font-weight: 300; font-size: 23px; color: var(--blue); }
  .hours__time { margin: 4px 0 20px; font-size: 26px; color: var(--ink); }

  .brand-mark { text-align: center; font-family: "Lato", sans-serif; font-weight: 400; color: var(--brand); letter-spacing: 1px; line-height: 1.2; }
  .brand-mark__dot { display: block; margin: 0 auto 14px; border-radius: 50%; border: 2px solid var(--brand); }
  .brand-mark--small { position: absolute; left: 0; right: 0; top: 290px; font-size: 22px; }
  .brand-mark--small .brand-mark__dot { width: 58px; height: 58px; }
  .brand-mark--large { position: absolute; left: 0; right: 0; top: 60px; font-size: 30px; }
  .brand-mark--large .brand-mark__dot { width: 110px; height: 110px; margin-bottom: 26px; }

  .contact { position: absolute; left: 0; right: 0; top: 498px; text-align: center; font-size: 16.5px; color: var(--ink); }
  .contact__icon { display: block; margin: 0 auto 4px; }
  .contact__line + .contact__icon { margin-top: 18px; }
  .photo--puppies {
    position: absolute; left: 0; right: 0; top: 620px; bottom: 20px;
    background: linear-gradient(180deg, rgba(255,255,255,1) 0%, #e9e9e9 45%, #d2d2d2 100%);
  }

  /* cover panel */
  .tagline-band {
    position: absolute; left: 0; right: 0; top: 365px; height: 116px;
    background: var(--blue); color: #fff;
    display: flex; align-items: center; justify-content: center; text-align: center;
    padding: 0 26px;
    font-family: "Oswald", sans-serif; font-weight: 300; font-size: 20px; line-height: 24px;
  }
  .address { position: absolute; left: 0; right: 0; top: 522px; text-align: center; font-size: 21px; line-height: 27px; }
  .address__text { margin: 18px 0; }
  .cover-web { position: absolute; left: 0; right: 0; top: 740px; text-align: center; font-size: 16px; }
</style>
</head>
<body>
  <main class="brochure">
    <section class="panel panel--mission">
      <div class="photo-grid">
        <div class="photo photo--dogs" role="img" aria-label="Photo of two beagle puppies running"></div>
        <div class="photo photo--cat-bowl" role="img" aria-label="Photo of a fluffy cat eating from a yellow bowl"></div>
        <div class="photo photo--kittens" role="img" aria-label="Photo of two kittens on a blanket"></div>
        <div class="photo photo--grey-cat" role="img" aria-label="Black and white photo of a resting cat"></div>
      </div>
      <h2 class="section-title"><span class="flourish" role="img" aria-label="Decorative flourish"></span>Our Mission<span class="flourish" role="img" aria-label="Decorative flourish"></span></h2>
      <p class="mission-text">is to care for your pet in the best way possible when you are away. We provide a unique social experience for dogs and create a new standard for dog care. Our Kitty condo provides a safe and quiet atmosphere for your kitty. We have set out to create a facility that exemplifies what we ourselves would want for our own best friends. Your pet will have a fun, safe place to play during the day and a secure night time environment when lodging with us. Our staff will go to any lengths to make our guest's stay a true delight. Our professional spa and grooming salon offers a wide range of services for your dog and cat. Our experienced groomers are friendly and knowledgeable and have the expertise to help your pet look and feel its best while exceeding your expectations.</p>
      <div class="bottom-band"></div>
    </section>

    <section class="panel panel--middle">
      <div class="hours">
        <span class="ornament" role="img" aria-label="Decorative scroll ornament"></span>
        <p class="hours__label">Hours of Operation</p>
        <p class="hours__time">Monday 7:30am- 6:30pm</p>
        <span class="ornament" role="img" aria-label="Decorative scroll ornament"></span>
      </div>
      <div class="brand-mark brand-mark--small">
        <span class="brand-mark__dot"></span>
        HOLLANDALE PET<br>MANOR &amp; SPA
      </div>
      <div class="contact">
        <svg class="contact__icon" width="20" height="20" viewBox="0 0 20 20" fill="none" stroke="#85abd2" stroke-width="1.3" aria-hidden="true">
          <circle cx="10" cy="10" r="8.5"/><ellipse cx="10" cy="10" rx="3.8" ry="8.5"/><path d="M1.5 10h17M3 5.5h14M3 14.5h14"/>
        </svg>
        <p class="contact__line">www.hollandalepetmanorandspa.com</p>
        <svg class="contact__icon" width="22" height="16" viewBox="0 0 22 16" fill="none" stroke="#85abd2" stroke-width="1.3" aria-hidden="true">
          <rect x="1" y="1" width="20" height="14"/><path d="M1 1l10 8 10-8"/>
        </svg>
        <p class="contact__line">info@hollandalepetmanorandspa.com</p>
      </div>
      <div class="photo--puppies" role="img" aria-label="Soft photo of two white puppies touching noses"></div>
      <div class="bottom-band"></div>
    </section>

    <section class="panel panel--cover">
      <div class="brand-mark brand-mark--large">
        <span class="brand-mark__dot"></span>
        HOLLANDALE PET<br>MANOR &amp; SPA
      </div>
      <p class="tagline-band">When it comes to your pet, we will stop at nothing to keep them healthy, happy and well-loved</p>
      <div class="address">
        <span class="ornament" role="img" aria-label="Decorative scroll ornament"></span>
        <p class="address__text">218 North Willow Lane<br>Hollandale, OH 43027</p>
        <span class="ornament" role="img" aria-label="Decorative scroll ornament"></span>
      </div>
      <p class="cover-web">www.hollandalepetmanorandspa.com</p>
    </section>
  </main>
</body>
</html>
```